Money Mindset Podcast needs fun, creative cover art

Launching a new podcast called 'Turning the Page on Savings' - aimed at an audience 30-50 who are interested in the practicalities of managing their money but also the more mental and emotional aspects.
Looking for something not too serious, warm and friendly.

Must be easy to read on phone screens
3000 x 3000 in size
Avoid currency symbols $, £ etc, as may have an international audience

Target Market(s)

Podcast listeners age 30-50 starting in the UK but then worldwide. Probably 60:40 female bias

Industry/Entity Type

Life Coaching

Font styles to use
Serif
Sans Serif

Colors
cadf82
fee18a
acd037
85cae6
eea4c8
f59195
85acd3

Requirements
Must have
• Simple, clear design. Easy to read on variety of devices. 3000 x 3000
Appeal to those with a spiritual or emotional interests
Nice to have
• Stand out among other money related podcasts
Maybe play around with clouds, lightbulbs and clearing skies
Should not have
• Currency symbols such as $ or £
Be too corporate or bank like
Stock images

```html
<!DOCTYPE html>
<html lang="en">
<head>
<meta charset="utf-8">
<title>Turning the Page on Savings — Podcast Cover</title>
<link rel="stylesheet" href="https://fonts.googleapis.com/css2?family=Bebas+Neue&display=swap">
<style>
  :root {
    --backdrop-deep: #0f4486;
    --backdrop-mid: #1b5fa8;
    --backdrop-light: #3f8acb;
    --backdrop-glow: #85acd3;
    --table-light: #ece6da;
    --table-shade: #d3c7b3;
    --title-white: #ffffff;
    --title-sand: #cdbf9f;
    --title-navy: #1b3a6b;
    --dice-wood: #e2cba6;
    --dice-wood-dark: #c2a57b;
  }
  html, body {
    margin: 0;
    padding: 0;
    width: 1200px;
    height: 1200px;
    overflow: hidden;
    background: var(--backdrop-deep);
  }
  .cover {
    position: relative;
    width: 1200px;
    height: 1200px;
    overflow: hidden;
    background: radial-gradient(ellipse 70% 60% at 55% 58%, var(--backdrop-light) 0%, var(--backdrop-mid) 45%, var(--backdrop-deep) 100%);
  }
  .tabletop {
    position: absolute;
    left: 0;
    right: 0;
    top: 930px;
    bottom: 0;
    background: linear-gradient(180deg, rgba(236,230,218,0.4) 0%, var(--table-shade) 18%, var(--table-light) 100%);
    filter: blur(3px);
  }
  .dice-stack {
    position: absolute;
    left: 186px;
    top: 330px;
    width: 250px;
    height: 786px;
    border-radius: 34px;
    background: linear-gradient(90deg, var(--dice-wood-dark) 0%, var(--dice-wood) 35%, var(--dice-wood) 70%, var(--dice-wood-dark) 100%);
  }
  .title {
    position: absolute;
    inset: 0;
    width: 1200px;
    height: 1200px;
  }
  .title text {
    font-family: "Bebas Neue", "Oswald", sans-serif;
    font-size: 252px;
  }
  .title .line-right { text-anchor: end; }
  .title .word-white { fill: var(--title-white); }
  .title .word-sand { fill: var(--title-sand); }
  .title .word-navy { fill: var(--title-navy); }
</style>
</head>
<body>
  <main class="cover">
    <div class="tabletop"></div>
    <div class="dice-stack" role="img" aria-label="Stack of four wooden letter dice on a table, turned to spell fake and fact"></div>
    <svg class="title" viewBox="0 0 1200 1200" role="heading" aria-level="1" aria-label="Turning the Page on Savings">
      <text class="line-right word-white" x="1008" y="278" textLength="760" lengthAdjust="spacingAndGlyphs">TURNING</text>
      <text class="line-right word-white" x="1008" y="494">THE</text>
      <text class="line-right word-sand" x="1008" y="698">PAGE</text>
      <text class="line-right word-white" x="1008" y="912">ON</text>
      <text class="word-navy" x="488" y="1122" textLength="520" lengthAdjust="spacingAndGlyphs">SAVINGS</text>
    </svg>
  </main>
</body>
</html>
```